Creative Business Card for my Sail Boat.. Tide & Drift

Going to order PLASTIC business cards for my boat.. she is a sailing vessel catamaran named Tide & Drift..

Target Market(s)

to impress other boaters with a unique designed plastic card

Contact Information for Business Card

S/V Tide & Drift
Captain Carl Denby
denby@carl.example
Mobile/WhatsApp 1-555-318-7620
www.sailtideanddrift.example

Requirements
Must have
• Cool colors. logo.. and info in Business Card Details.. Thanks! Utilize clear or cloudy plastic in design. Thanks

```html
<!DOCTYPE html>
<html lang="en">
<head>
<meta charset="utf-8">
<title>Tide &amp; Drift – Business Card</title>
<link rel="stylesheet" href="https://fonts.googleapis.com/css2?family=Comic+Neue:wght@400;700&family=Arimo:wght@400&display=swap">
<style>
  :root {
    --page-bg: #e4e6e9;
    --frost-light: #f7f8f9;
    --frost-mid: #e3e5e8;
    --frost-dark: #cdd1d5;
    --sea-blue: #2f7fb5;
    --wave-edge: #e4f3f8;
    --sand: #c9ab8c;
    --logo-taupe: #9a8878;
    --white: #ffffff;
  }
  * { margin: 0; padding: 0; box-sizing: border-box; }
  html, body {
    width: 1200px; height: 1200px; overflow: hidden;
    background: var(--page-bg);
  }
  .card {
    position: absolute;
    left: 100px; top: 314px;
    width: 1000px; height: 572px;
    border-radius: 28px;
    overflow: hidden;
    box-shadow: 0 12px 30px rgba(0,0,0,0.18);
    background: linear-gradient(160deg, var(--frost-light) 0%, var(--frost-mid) 55%, var(--frost-dark) 100%);
  }
  .card-art { position: absolute; inset: 0; width: 100%; height: 100%; }
  .brand {
    position: absolute; left: 80px; top: 120px;
    display: flex; align-items: center; gap: 18px;
  }
  .brand-name {
    font-family: "Comic Neue", cursive;
    font-weight: 700; font-size: 64px; line-height: 1;
    color: var(--logo-taupe);
  }
  .brand-dot {
    width: 34px; height: 34px; border-radius: 50%;
    background: var(--logo-taupe);
  }
  .details {
    position: absolute; left: 590px; top: 190px;
    font-family: "Comic Neue", cursive;
  }
  .vessel { font-size: 40px; font-weight: 400; color: var(--sand); line-height: 1.1; }
  .captain { font-size: 32px; font-weight: 700; color: var(--white); margin-top: 6px; }
  .contact-list { list-style: none; margin-top: 34px; }
  .contact-item {
    display: flex; align-items: center; gap: 18px;
    font-family: "Arimo", sans-serif; font-size: 24px; color: var(--white);
    margin-bottom: 26px;
  }
  .contact-icon { width: 38px; height: 38px; flex: none; }
</style>
</head>
<body>
  <div class="card">
    <svg class="card-art" viewBox="0 0 1000 572" aria-hidden="true">
      <path d="M0 400 C 200 385, 300 345, 420 260 C 540 175, 640 100, 1000 95 L1000 572 L0 572 Z" fill="var(--sea-blue)"/>
      <path d="M0 400 C 200 385, 300 345, 420 260 C 540 175, 640 100, 1000 95" fill="none" stroke="var(--wave-edge)" stroke-width="10"/>
    </svg>
    <svg class="card-art" viewBox="0 0 1000 572" role="img" aria-label="Ship's wheel emblem">
      <circle cx="335" cy="330" r="92" fill="var(--wave-edge)"/>
      <circle cx="335" cy="330" r="82" fill="var(--sea-blue)"/>
    </svg>

    <div class="brand">
      <span class="brand-name">Tide &amp; Drift</span>
      <span class="brand-dot"></span>
    </div>

    <div class="details">
      <div class="vessel">S/V Tide &amp; Drift</div>
      <div class="captain">Captain Carl Denby</div>
      <ul class="contact-list">
        <li class="contact-item">
          <svg class="contact-icon" viewBox="0 0 38 38" aria-hidden="true">
            <circle cx="19" cy="19" r="16" fill="none" stroke="var(--sand)" stroke-width="2.5"/>
            <path d="M13 12 l4 -1 l2 5 l-2.5 1.5 a10 10 0 0 0 5 5 l1.5 -2.5 l5 2 l-1 4 a14 14 0 0 1 -14 -14z" fill="var(--sand)"/>
          </svg>
          <span>1-555-318-7620</span>
        </li>
        <li class="contact-item">
          <svg class="contact-icon" viewBox="0 0 38 38" aria-hidden="true">
            <circle cx="19" cy="19" r="16" fill="none" stroke="var(--sand)" stroke-width="2.5"/>
            <text x="19" y="26" text-anchor="middle" font-family="Arimo, sans-serif" font-size="20" fill="var(--sand)">@</text>
          </svg>
          <span>denby@carl.example</span>
        </li>
      </ul>
    </div>
  </div>
</body>
</html>
```